Need a flyer created for a charity motorcycle run.

I need a "First Annual Gus Tarn Black Friday Fun Run" flyer/poster created. It is to benefit the wild fire victims at Lake Berryessa where Gus spent all of his time on his boat. Gus died about 18 mos ago from brain cancer. I have a few pics of him on his Kestrow at Vandmere. I have the verbiage needed (due to Covid, there are several restrictions) but it needs some word smithing. This flyer will be emailed to those without social media accounts and also posted on FB as an invite so we can get a good count because space is limited.

Please make sure all designs have both pictures in them. Thanks

```html
<!DOCTYPE html>
<html lang="en">
<head>
<meta charset="utf-8">
<title>First Annual Gus Tarn Black Friday Fun Run</title>
<link rel="stylesheet" href="https://fonts.googleapis.com/css2?family=Open+Sans:wght@400;600;700;800&family=Russo+One&family=Dancing+Script:wght@500&display=swap">
<style>
  :root {
    --ink-black: #0b0b0c;
    --blue-bright: #1ba0e2;
    --blue-deep: #0a5a9c;
    --blue-text: #2aa6e6;
    --white: #ffffff;
    --chrome-light: #f4f6f8;
    --chrome-mid: #9aa3ab;
    --chrome-dark: #3f464c;
  }
  * { margin: 0; padding: 0; box-sizing: border-box; }
  html, body { width: 970px; height: 1200px; overflow: hidden; background: var(--ink-black); }
  .flyer {
    position: relative;
    width: 970px;
    height: 1200px;
    overflow: hidden;
    font-family: "Open Sans", Arial, sans-serif;
    color: var(--white);
    background: radial-gradient(ellipse at 50% 30%, #3a3b3d 0%, #1c1d1f 45%, var(--ink-black) 85%);
  }
  .title-frame {
    position: absolute;
    left: 63px; top: 106px;
    width: 864px; height: 176px;
    border: 1.5px solid var(--blue-deep);
  }
  .title-frame::before {
    content: "";
    position: absolute;
    left: 290px; top: -4px;
    width: 284px; height: 8px;
    background: #2e2f31;
  }
  .eyebrow {
    position: absolute; top: 44px; width: 100%;
    text-align: center;
    font-weight: 700; font-size: 23px; letter-spacing: 1px;
  }
  .chrome {
    font-family: "Russo One", Arial, sans-serif;
    text-transform: uppercase;
    background: linear-gradient(180deg, var(--chrome-light) 0%, var(--chrome-light) 40%, var(--chrome-dark) 52%, var(--chrome-mid) 70%, var(--chrome-light) 100%);
    -webkit-background-clip: text; background-clip: text;
    color: transparent;
    -webkit-text-stroke: 1px #1a1c1e;
  }
  .honoree {
    position: absolute; top: 80px; width: 100%;
    text-align: center; font-size: 48px; letter-spacing: 4px;
  }
  .event-name {
    position: absolute; top: 136px; width: 100%;
    text-align: center; font-size: 104px; letter-spacing: 2px; line-height: 1;
  }
  .event-subtitle {
    position: absolute; top: 226px; width: 100%;
    text-align: center;
    font-family: "Dancing Script", cursive;
    font-size: 64px; color: var(--blue-bright); line-height: 1;
  }
  .story {
    position: absolute; top: 308px; left: 110px; width: 750px;
    text-align: center; font-size: 15.5px; line-height: 1.5;
  }
  .date-banner {
    position: absolute; top: 430px; left: 290px;
    width: 390px; height: 40px;
    background: linear-gradient(90deg, var(--blue-deep), var(--blue-bright) 45%, var(--blue-deep));
    transform: skewX(-14deg);
    box-shadow: 0 0 0 2px rgba(255,255,255,0.15);
  }
  .date-banner span {
    display: block; transform: skewX(14deg);
    text-align: center; line-height: 40px;
    font-weight: 700; font-size: 22px; letter-spacing: 0.5px;
  }
  .invite {
    position: absolute; top: 484px; left: 170px; width: 630px;
    text-align: center; color: var(--blue-text);
    font-size: 21px; line-height: 1.4;
  }
  .art { position: absolute; left: 0; top: 0; }
  .details {
    position: absolute; left: 36px; top: 640px; width: 306px;
  }
  .detail { margin-bottom: 12px; }
  .detail h2 {
    display: flex; align-items: center; gap: 7px;
    font-weight: 800; font-size: 17px; letter-spacing: 0.3px;
    margin-bottom: 3px;
  }
  .detail h2 svg { width: 22px; height: 22px; flex: none; }
  .detail p { font-size: 11px; line-height: 1.25; margin-bottom: 4px; }
  .pay-bar {
    position: absolute; left: 0; top: 1086px;
    width: 470px; height: 60px;
    background: linear-gradient(90deg, var(--blue-bright), var(--blue-deep));
    clip-path: polygon(0 0, 100% 0, 95% 100%, 0 100%);
    font-size: 21px; line-height: 60px; padding-left: 30px;
  }
</style>
</head>
<body>
<main class="flyer">
  <div class="title-frame"></div>
  <p class="eyebrow">FIRST ANNUAL</p>
  <h1>
    <span class="honoree chrome">Gus Tarn</span>
    <span class="event-name chrome">Black Friday</span>
    <span class="event-subtitle">Fun Run</span>
  </h1>

  <p class="story">If any of you knew Gus Tarn, you knew “Black Friday”. As a carpenter for local 22, he was blessed with the extra holidays. Well that became the name of his true tangible love, His boat! He would spend almost every free minute he had on that beauty out on Lake Berryessa! As time went on he added onto that and incorporated Friends Giving on Pinecrest Drive @ Cedar Flat! KOVA would be absolutely heart broken to see so many of his memories and friends hurt by the recent Fires...</p>

  <div class="date-banner"><span>SATURDAY NOVEMBER 28</span></div>

  <p class="invite">So to Honor him..<br>Let’s ride to Heron Rock Saturday November 28 and have some egg rolls while a DJ plays some music.</p>

  <svg class="art" width="970" height="1200" viewBox="0 0 970 1200">
    <defs>
      <linearGradient id="ride-tones" x1="0" y1="0" x2="1" y2="1">
        <stop offset="0" stop-color="#c9ccd0"/>
        <stop offset="0.45" stop-color="#4c5a7a"/>
        <stop offset="1" stop-color="#1e2438"/>
      </linearGradient>
      <linearGradient id="portrait-tones" x1="0" y1="0" x2="0" y2="1">
        <stop offset="0" stop-color="#9fb9cf"/>
        <stop offset="0.5" stop-color="#c98f74"/>
        <stop offset="1" stop-color="#a96a52"/>
      </linearGradient>
    </defs>
    <circle cx="835" cy="1045" r="462" fill="none" stroke="var(--blue-deep)" stroke-width="18"/>
    <circle cx="835" cy="1045" r="448" fill="none" stroke="#d8dadc" stroke-width="6"/>
    <circle cx="835" cy="1045" r="445" fill="url(#ride-tones)" role="img" aria-label="Photo of Gus seated on his Kestrow motorcycle at Vandmere"/>
    <circle cx="840" cy="646" r="108" fill="#6b6f74"/>
    <circle cx="840" cy="646" r="100" fill="#e4e6e8"/>
    <circle cx="840" cy="646" r="93" fill="url(#portrait-tones)" role="img" aria-label="Portrait photo of Gus at Lake Berryessa"/>
  </svg>

  <section class="details">
    <div class="detail">
      <h2><svg viewBox="0 0 24 24" fill="none" stroke="var(--blue-bright)" stroke-width="2"><circle cx="12" cy="12" r="10"/><path d="M12 6v6l4 2"/></svg>TIME</h2>
      <p>- 50 bikes are invited to meet us @9:30 depart at 10 (location will be announced closer to date because of limited capacity but is confirmed)</p>
      <p>- Cars will meet @10 in Valley Ridge Community College parking lot. Depart 10:30 to head up the hill.</p>
      <p>- We will all arrive approx 11:30 at Heron Rock Bar to remember the good times and raffle off some amazing prizes!!</p>
    </div>
    <div class="detail">
      <h2><svg viewBox="0 0 24 24" fill="none" stroke="var(--blue-bright)" stroke-width="2"><rect x="4" y="3" width="14" height="18" rx="1"/><path d="M7 8h8M7 12h8M7 16h5"/></svg>REGISTRATION</h2>
      <p>Registration is $25 per person which will include 1 egg roll and a Beer or Soda.</p>
    </div>
    <div class="detail">
      <h2><svg viewBox="0 0 24 24" fill="none" stroke="var(--blue-bright)" stroke-width="2"><path d="M8 21v-4c-2-1.5-3-3.5-3-6a7 7 0 0 1 14 0l2 4h-2v3h-3v3"/></svg>COVID 19</h2>
      <p>100% Covid compliant. Face mask will be required while we are entertained outside in the parking lot. There is a possibility of being rained out given the time of year!</p>
    </div>
    <div class="detail">
      <h2><svg viewBox="0 0 24 24" fill="none" stroke="var(--blue-bright)" stroke-width="2"><circle cx="12" cy="9" r="6"/><path d="M8 14l-2 8 6-3 6 3-2-8"/></svg>PRIZES</h2>
      <p>Prizes will still be available to any registered guest and can be drawn Live on SocialFeed if rained out! All proceeds will be given to Walt @ Heron Rock to distribute to the verified Fire Victims of Lake Berryessa.</p>
    </div>
  </section>

  <div class="pay-bar">You can PayKit me @RoadsideEscapes</div>
</main>
</body>
</html>
```